Lorna Tess Tresses Fancy Business Card’s

I want my business cards to be elite, original and very classy. I want the business cards to match the colors of my logo and to match the design posted. I would love the design of the picture I posted

I want the card all white .
The dripping on the top of the card I want it to match the pink color in my logo that’s also posted .
I need my logo on the business card !
I need my Instagram- @lorna.tess.tresses__
And my phone number - 582 907 3365

Target Market(s)

My target market is young woman age 23 to older woman to the age of 65
I want both older and younger women to love my design . I don’t want any cheap looking business cards

Industry/Entity Type

Hair And Beauty

Contact Information for Business Card

Add my logo
Add my Instagram- @lorna.tess.tresses__
My number - 582 907 3365
My website- www.lornatesstresses.example

Font styles to use
Serif
Script

Colors
ffffff
e667a6
e34298

Requirements
Must have
• The business cards must have my logo, my number , my website, and my Instagram!
Nice to have
• Nice to have glitter words that match my logo
• The business cards must look classy and mature
• I want them to be very unique!!
Should not have
• Should not have any colors that doesn’t match my logo ! This is very important! Please

```html
<!DOCTYPE html>
<html lang="en">
<head>
<meta charset="utf-8">
<title>Lorna Tess Tresses — Business Card</title>
<link rel="stylesheet" href="https://fonts.googleapis.com/css2?family=Libre+Baskerville:wght@400&display=swap">
<style>
  :root {
    --backdrop: #e9e6e3;
    --card: #727272;
    --pink: #f4c6de;
    --soft-grey: #d2d2d2;
    --card-shadow: rgba(0, 0, 0, 0.35);
  }
  html, body {
    margin: 0;
    padding: 0;
    width: 1189px;
    height: 1200px;
    overflow: hidden;
    background: var(--backdrop);
  }
  .canvas {
    position: relative;
    width: 1189px;
    height: 1200px;
    font-family: "Libre Baskerville", "Times New Roman", serif;
  }
  .card {
    position: absolute;
    left: 169px;
    width: 852px;
    height: 486px;
    background: var(--card);
    box-shadow: 0 2px 6px var(--card-shadow);
  }
  .card--front { top: 111px; }
  .card--back  { top: 641px; }

  .brand-name {
    position: absolute;
    left: 0;
    right: 0;
    top: 212px;
    margin: 0;
    text-align: center;
    font-size: 52px;
    font-weight: 400;
    color: var(--pink);
    letter-spacing: 0.01em;
  }

  .contact-rule {
    position: absolute;
    left: 0;
    top: 0;
  }
  .contact-list {
    position: absolute;
    left: 0;
    right: 0;
    top: 223px;
    margin: 0;
    padding: 0;
    list-style: none;
    text-align: center;
    color: var(--soft-grey);
  }
  .contact-list li { margin: 0; }
  .contact-handle { font-size: 24px; line-height: 34px; }
  .contact-phone  { font-size: 24px; line-height: 34px; }
  .contact-web {
    margin-top: 2px !important;
    font-size: 20px;
    line-height: 34px;
    letter-spacing: 0.42em;
    padding-left: 0.42em;
  }
  .contact-web .domain { color: var(--pink); }
</style>
</head>
<body>
<main class="canvas">
  <section class="card card--front" aria-label="Card front">
    <h1 class="brand-name">Lorna Tess Tresses</h1>
  </section>

  <section class="card card--back" aria-label="Card back">
    <svg class="contact-rule" width="852" height="486" viewBox="0 0 852 486" aria-hidden="true">
      <g fill="none" stroke="var(--pink)" stroke-width="2.5">
        <line x1="157" y1="186" x2="352" y2="186"/>
        <line x1="499" y1="186" x2="695" y2="186"/>
        <circle cx="373" cy="186" r="21"/>
        <circle cx="425" cy="186" r="21"/>
        <circle cx="477" cy="186" r="21"/>
        <circle cx="373" cy="186" r="16" stroke-width="1.5"/>
        <circle cx="425" cy="186" r="16" stroke-width="1.5"/>
        <circle cx="477" cy="186" r="16" stroke-width="1.5"/>
        <path d="M420 177 q-3 2 -1 8 q3 8 9 11 q3 1 5 -2 l-3 -3 q-2 1 -3 0 q-3 -3 -4 -6 q0 -2 1 -2 l-2 -4 z" stroke-width="1.6" stroke-linejoin="round"/>
        <g stroke-width="1.4">
          <circle cx="477" cy="186" r="9"/>
          <ellipse cx="477" cy="186" rx="4" ry="9"/>
          <line x1="468" y1="186" x2="486" y2="186"/>
          <line x1="470" y1="181" x2="484" y2="181"/>
          <line x1="470" y1="191" x2="484" y2="191"/>
        </g>
      </g>
    </svg>
    <ul class="contact-list">
      <li class="contact-handle">@lorna.tess.tresses__</li>
      <li class="contact-phone">582 907 3365</li>
      <li class="contact-web">www.<span class="domain">lornatesstresses</span>.example</li>
    </ul>
  </section>
</main>
</body>
</html>
```